Verantix - Solution provider in business consulting

Verantix is a swiss based company providing solutions for developing markets. The business covers various fields of business consulting, such as supply chain, product costs, quality management and manufacturing management. The Business operates in a efficient, straight and solution oriented manner.
The final design should communicate these characteristics. Asian people as well as as western people shall identify the qualities of the company at first sight.
The customer needs business cards with a simple view but an recognizable design, printed in high quality. Engraved elements such as the globe or simple words are possible.
Available colors are: (RAL)
102/102/102
51/102/102
153/204/153
255/102/51
Font: Calibri
Industry/Entity Type
Business
Look and feel
Each slider illustrates characteristics of the customer's brand and the style your logo design should communicate.

```html
<!DOCTYPE html>
<html lang="en">
<head>
<meta charset="utf-8">
<title>Verantix – Business Card</title>
<link rel="stylesheet" href="https://fonts.googleapis.com/css2?family=Open+Sans:wght@400;600&display=swap">
<style>
  :root {
    --backdrop: #d6d6d6;
    --card: #ececec;
    --ink: #666666;
    --ink-strong: #5c5c5c;
    --rule: #6e6e6e;
    --globe-light: #f3f3f3;
    --globe-shade: #e2e2e2;
  }
  * { margin: 0; padding: 0; box-sizing: border-box; }
  html, body {
    width: 1200px; height: 1000px; overflow: hidden;
    background: var(--backdrop);
    font-family: "Open Sans", Calibri, sans-serif;
    color: var(--ink);
  }
  .card {
    position: absolute; left: 100px; top: 203px;
    width: 1000px; height: 594px;
    background: var(--card);
    border-radius: 30px;
    box-shadow: 0 6px 18px rgba(0,0,0,0.18);
    overflow: hidden;
  }
  .globe-relief {
    position: absolute; left: 41px; top: 45px;
    width: 418px; height: 418px; border-radius: 50%;
    background: radial-gradient(circle at 70% 35%, var(--globe-light), var(--globe-shade));
    box-shadow: inset 2px 2px 3px rgba(255,255,255,0.8), inset -2px -2px 4px rgba(0,0,0,0.06);
  }
  .holder { position: absolute; left: 50px; top: 152px; }
  .holder-name { font-size: 33px; font-weight: 600; color: var(--ink-strong); line-height: 1.1; }
  .holder-role { font-size: 25px; line-height: 1.3; }
  .brand-name {
    position: absolute; right: 48px; top: 78px;
    font-size: 72px; font-weight: 400; color: var(--ink); line-height: 1;
  }
  .address {
    position: absolute; right: 48px; top: 284px;
    text-align: right; font-size: 25px; line-height: 33px;
  }
  .contact-list {
    position: absolute; right: 45px; top: 408px;
    list-style: none; text-align: right; font-size: 25px; line-height: 39px;
  }
  .contact-list li { display: flex; justify-content: flex-end; align-items: center; gap: 10px; }
  .contact-list svg { width: 18px; height: 18px; fill: var(--ink); }
  .footer-row {
    position: absolute; left: 50px; right: 48px; top: 523px;
    display: flex; align-items: center; gap: 14px; font-size: 25px;
  }
  .footer-row strong { font-weight: 600; }
  .footer-rule { flex: 1; height: 2px; background: var(--rule); }
</style>
</head>
<body>
  <article class="card">
    <div class="globe-relief" role="img" aria-label="Embossed globe relief showing East Asia and surrounding coastlines"></div>

    <div class="holder">
      <p class="holder-name">Marten Rhyner</p>
      <p class="holder-role">CEO</p>
    </div>

    <p class="brand-name">Verantix</p>

    <address class="address" style="font-style:normal">
      Verantix GmbH<br>
      Lindenweg 14<br>
      9247 Talbach
    </address>

    <ul class="contact-list">
      <li>+41 79 582 3317
        <svg viewBox="0 0 18 18" aria-label="Mobile"><rect x="5" y="1" width="8" height="16" rx="1.5"/><rect x="6.5" y="3" width="5" height="9" fill="#ececec"/></svg>
      </li>
      <li>+41 71 834 6620
        <svg viewBox="0 0 18 18" aria-label="Phone"><path d="M2 6c0-2 3-3 7-3s7 1 7 3v1h-3V5.5H5V7H2z"/><path d="M4 8h10l2 7H2z"/><circle cx="9" cy="11.5" r="2" fill="#ececec"/></svg>
      </li>
      <li>marten.rhyner@verantix.ch
        <svg viewBox="0 0 18 18" aria-label="Email"><rect x="1" y="4" width="16" height="11"/><path d="M1.5 4.5L9 10l7.5-5.5" stroke="#ececec" stroke-width="1.3" fill="none"/></svg>
      </li>
    </ul>

    <div class="footer-row">
      <span>www.<strong>verantix</strong>.ch</span>
      <span class="footer-rule"></span>
    </div>
  </article>
</body>
</html>
```